Website Design for BRAVO FREIGHTWAY

Hello. We are a Freight Brokage business in the transportation and logistics industry in the USA. Company name is BRAVO FREIGHTWAY. I'm looking to have a 5 page or less website built. Must have HOME, SHIPPERS, CARRIERS, ABOUT and CONTACT US.. I have additional information that needs to be placed in the footer of the website. Company address, contact info privacy and terms and conditions Need nice, vibrant looking site. The website needs to be a fully functionable site that is built and coded for wordpress and ready for hosting. Please visit these link for you to have an idea of the look and feel I want. www.tolvanhaulage.example www.corvel-transit.example. Will have logo concept in 2 days for upload. As time goes by I will supply more content and the layout of the respective pages.

```html
<!DOCTYPE html>
<html lang="en">
<head>
<meta charset="utf-8">
<title>Bravo Freightway – Freight Brokerage Business</title>
<link rel="stylesheet" href="https://fonts.googleapis.com/css2?family=Orbitron:wght@700;800;900&family=Poppins:wght@400;500;600;700&display=swap">
<style>
:root{
  --red:#d8102a;
  --red-deep:#b80c22;
  --navy:#1b3a9c;
  --blue:#1442a8;
  --ink:#1d1d1d;
  --text:#3b3b3b;
  --grey-bg:#ececec;
  --field:#ececec;
  --white:#ffffff;
  --purple:#6a1f7a;
}
*{box-sizing:border-box;margin:0;padding:0}
html,body{width:1200px;height:4076px;overflow:hidden}
body{font-family:"Poppins",sans-serif;color:var(--text);background:var(--white);position:relative}
.display{font-family:"Orbitron",sans-serif;font-weight:900;letter-spacing:1px;text-transform:uppercase}
section,header,footer{position:absolute;left:0;width:1200px}

/* header */
.site-header{top:0;height:100px;background:var(--white)}
.brand{position:absolute;left:105px;top:20px;display:flex;align-items:center;gap:14px}
.brand-mark{width:46px;height:46px;background:var(--red)}
.brand-name{font-family:"Orbitron",sans-serif;font-weight:900;font-size:21px;color:var(--navy);letter-spacing:1px}
.brand-tag{font-size:13px;font-weight:500;color:var(--ink);margin-top:2px}
.main-nav{position:absolute;left:550px;top:38px;display:flex;gap:42px;font-size:15px;color:var(--ink)}
.btn-contact{position:absolute;left:939px;top:27px;width:156px;height:46px;background:var(--red);color:var(--white);font-family:"Orbitron",sans-serif;font-weight:800;font-size:14px;display:flex;align-items:center;justify-content:center;letter-spacing:1px}

/* hero */
.hero{top:100px;height:607px;overflow:hidden}
.hero svg{position:absolute;inset:0}
.hero-tag{position:absolute;left:465px;top:170px;width:294px;height:50px;background:var(--red);color:var(--white);font-weight:600;font-size:16px;display:flex;align-items:center;justify-content:center}
.hero-title{position:absolute;left:0;width:1200px;top:245px;text-align:center;color:var(--white);font-size:96px;line-height:96px}

/* feature cards */
.features{top:715px;height:345px}
.card{position:absolute;top:0;height:345px;width:293px;display:flex;align-items:flex-end;justify-content:center;padding-bottom:28px;text-align:center}
.card span{color:var(--white);font-family:"Orbitron",sans-serif;font-weight:800;font-size:15px;line-height:19px;letter-spacing:1px}
.arrow{position:absolute;top:158px;width:16px;height:16px;border-radius:50%;background:var(--white);display:flex;align-items:center;justify-content:center}
.arrow.right{background:var(--blue)}

/* about */
.about{top:1060px;height:335px}
.about h2{position:absolute;left:105px;top:72px;font-size:33px;line-height:42px;color:var(--navy)}
.about-copy{position:absolute;left:497px;top:72px;width:598px;font-size:14.5px;line-height:26px;text-align:justify}
.about-copy p+p{margin-top:10px}

/* banner */
.banner{top:1395px;height:535px}
.banner-photo{position:absolute;left:0;top:0;width:602px;height:535px;background:linear-gradient(135deg,#7d2a2a 0%,#5b6e8a 45%,#3b3f4b 100%)}
.banner-panel{position:absolute;left:602px;top:0;width:598px;height:535px;background:linear-gradient(180deg,#1846b0,#1239a0)}
.banner-panel h2{position:absolute;left:34px;top:70px;color:var(--white);font-size:26px;line-height:35px}
.banner-lead{position:absolute;left:34px;top:190px;width:530px;color:var(--white);font-weight:600;font-size:16px;line-height:27px}
.banner-body{position:absolute;left:34px;top:255px;width:530px;color:var(--white);font-size:14.5px;line-height:27px}
.btn-outline{position:absolute;left:34px;top:406px;width:166px;height:50px;border:2px solid var(--white);color:var(--white);font-family:"Orbitron",sans-serif;font-weight:800;font-size:14px;display:flex;align-items:center;justify-content:center;letter-spacing:1px}

/* trust */
.trust{top:1930px;height:507px}
.trust h2{position:absolute;top:82px;width:1200px;text-align:center;color:var(--navy);font-size:33px}
.trust-item{position:absolute;top:175px;width:300px;text-align:center}
.trust-icon{width:134px;height:134px;border-radius:50%;margin:0 auto;background:linear-gradient(135deg,#d8102a 0%,#8a1a5a 55%,#2b2f9c 100%);display:flex;align-items:center;justify-content:center}
.trust-item h3{margin-top:22px;font-family:"Orbitron",sans-serif;font-weight:800;font-size:17px;color:var(--ink);letter-spacing:1px}
.trust-item p{margin-top:12px;font-size:14px;line-height:22px}

/* survey */
.survey{top:2437px;height:547px;background:var(--grey-bg)}
.survey-photo{position:absolute;left:147px;top:95px;width:366px;height:366px;border-radius:50%;background:linear-gradient(var(--white),var(--white)) padding-box,linear-gradient(135deg,#2b2f9c,#d8102a) border-box;border:3px solid transparent;padding:6px}
.survey-photo div{width:100%;height:100%;border-radius:50%;background:linear-gradient(160deg,#a9c3e6 0%,#e7e9ee 45%,#8f939b 100%)}
.survey h2{position:absolute;left:595px;top:116px;font-size:27px;color:var(--navy)}
.survey-copy{position:absolute;left:595px;top:165px;width:456px;font-size:14.5px;line-height:24px;text-align:justify}
.btn-red{position:absolute;left:595px;top:375px;width:166px;height:48px;background:var(--red);color:var(--white);font-family:"Orbitron",sans-serif;font-weight:800;font-size:14px;display:flex;align-items:center;justify-content:center;letter-spacing:1px}

/* contact */
.contact{top:2984px;height:641px;background:linear-gradient(180deg,#dc1430,#d10f29)}
.contact h2{position:absolute;top:80px;width:1200px;text-align:center;color:var(--white);font-size:27px}
.field{position:absolute;width:318px;height:50px;background:var(--field);font-size:12.5px;color:var(--ink);padding:16px 21px}
.field.message{width:993px;height:183px}
.btn-submit{position:absolute;left:535px;top:499px;width:133px;height:49px;border:2px solid var(--white);color:var(--white);font-family:"Orbitron",sans-serif;font-weight:800;font-size:14px;display:flex;align-items:center;justify-content:center;letter-spacing:1px}

/* footer */
.site-footer{top:3625px;height:451px;background:var(--white)}
.foot-brand{position:absolute;left:103px;top:52px;width:250px}
.foot-mark{width:70px;height:70px;background:var(--red);margin-left:70px}
.foot-name{margin-top:18px;font-family:"Orbitron",sans-serif;font-weight:900;font-size:18px;color:var(--navy);letter-spacing:.5px;text-align:center}
.foot-tag{font-size:12px;text-align:center;color:var(--ink);margin-top:2px}
.foot-about{margin-top:14px;font-size:13px;line-height:23px}
.foot-col{position:absolute;top:58px}
.foot-col h4{font-family:"Orbitron",sans-serif;font-weight:800;font-size:16px;color:var(--navy);letter-spacing:1px;margin-bottom:12px}
.foot-col li{list-style:none;font-size:14px;line-height:30px;color:var(--ink)}
.contact-info{font-size:13.5px;line-height:24px;color:var(--text);width:300px}
.contact-info b{color:var(--ink);font-weight:600}
.contact-info .row{display:flex;gap:6px;align-items:flex-start}
.contact-info .ind{padding-left:19px}
.contact-info svg{flex:none;margin-top:5px}
.foot-rule{position:absolute;left:103px;top:375px;width:993px;height:1px;background:#555}
.copyright{position:absolute;top:404px;width:1200px;text-align:center;font-size:14px;color:var(--ink)}
</style>
</head>
<body>

<header class="site-header">
  <div class="brand">
    <div class="brand-mark"></div>
    <div>
      <div class="brand-name">BRAVO FREIGHTWAY</div>
      <div class="brand-tag">Freight Brokerage Business</div>
    </div>
  </div>
  <nav class="main-nav"><span>Home</span><span>Shippers</span><span>Carriers</span><span>About</span></nav>
  <div class="btn-contact">CONTACT US</div>
</header>

<section class="hero">
  <svg width="1200" height="607" viewBox="0 0 1200 607">
    <defs>
      <linearGradient id="heroRight" x1="0" y1="0" x2="0" y2="1">
        <stop offset="0" stop-color="#4f6e8f"/>
        <stop offset="0.4" stop-color="#b06a3a"/>
        <stop offset="0.75" stop-color="#5b4a3a"/>
        <stop offset="1" stop-color="#2f3137"/>
      </linearGradient>
      <linearGradient id="heroLeft" x1="0" y1="0" x2="1" y2="1">
        <stop offset="0" stop-color="#6b5a48"/>
        <stop offset="0.5" stop-color="#4a4540"/>
        <stop offset="1" stop-color="#2c2b2a"/>
      </linearGradient>
    </defs>
    <rect width="1200" height="607" fill="url(#heroRight)" role="img" aria-label="Photo of a semi truck with a white trailer on a desert road at sunset"/>
    <polygon points="0,0 1120,0 0,607" fill="url(#heroLeft)" role="img" aria-label="Photo of a warehouse worker driving a forklift carrying boxes"/>
  </svg>
  <div class="hero-tag">FREIGHT BROKERAGE BUSINESS</div>
  <h1 class="hero-title display">BRAVO<br>FREIGHTWAY</h1>
</section>

<section class="features">
  <div class="card" style="left:8px;background:linear-gradient(180deg,#a4552e 0%,#2d3f7a 60%,#161a24 100%)" role="img" aria-label="Photo of a blue truck among shipping containers"><span>NATIONAL AND<br>REGIONAL CAPACITY</span></div>
  <div class="card" style="left:305px;background:linear-gradient(180deg,#6d6f73 0%,#b8a58a 55%,#2a2724 100%)" role="img" aria-label="Photo of warehouse shelves stacked with cartons"><span>COMPETITIVE<br>PRICES</span></div>
  <div class="card" style="left:602px;background:linear-gradient(180deg,#5f6670 0%,#8a5a40 55%,#1f1d1c 100%)" role="img" aria-label="Photo of a worker operating a forklift"><span>DEDICATED<br>REPRESENTATIVES</span></div>
  <div class="card" style="left:899px;background:linear-gradient(180deg,#d8dbe0 0%,#8a8c92 55%,#1e1f23 100%)" role="img" aria-label="Photo of a businesswoman holding a clipboard in a warehouse"><span>PROACTIVE<br>COMMUNICATION</span></div>
  <div class="arrow" style="left:12px"><svg width="8" height="8" viewBox="0 0 8 8"><path d="M5.5 1 2.5 4l3 3" fill="none" stroke="#333" stroke-width="1.6"/></svg></div>
  <div class="arrow right" style="left:1162px"><svg width="8" height="8" viewBox="0 0 8 8"><path d="M2.5 1l3 3-3 3" fill="none" stroke="#fff" stroke-width="1.6"/></svg></div>
</section>

<section class="about">
  <h2 class="display">ABOUT BRAVO<br>FREIGHTWAY</h2>
  <div class="about-copy">
    <p>Lorem ipsum dolor sit amet, consectetur adipiscing elit, sed do eiusmod tempor incididunt ut labore et dolore magna aliqua. Ut enim ad minim veniam, quis nostrud exercitation ullamco laboris nisi ut aliquip ex ea commodo consequat. Duis aute irure dolor in reprehenderit in voluptate velit esse cillum dolore eu fugiat nulla pariatur.</p>
    <p>Ut enim ad minim veniam . Duis aute irure dolor in reprehenderit in voluptate velit esse cillum dolore eu fugiat nulla pariatur.</p>
  </div>
</section>

<section class="banner">
  <div class="banner-photo" role="img" aria-label="Photo of two smiling truck drivers in caps standing in front of red trucks"></div>
  <div class="banner-panel">
    <h2 class="display">FULL TRUCK LOAD<br>SOLUTIONS THAT HELP YOU<br>DELIVER ON YOU RPROMISES</h2>
    <p class="banner-lead">Our extensive network of capacity stands ready to deliver your cargo on time every time!</p>
    <p class="banner-body">Lorem ipsum dolor sit amet, consectetur adipiscing elit, sed do eiusmod tempor incididunt ut labore et dolore magna aliqua. Ut enim ad minim veniam, quis nostrud exercitation ullamco laboris nisi ut aliquip ex ea commodo consequat. Duis aute irure dolor in reprehenderit in voluptate velit esse cillum dolore eu fugiat nulla pariatur.</p>
    <div class="btn-outline">READ MORE</div>
  </div>
</section>

<section class="trust">
  <h2 class="display">TRUSTED BY 950+ HAPPY CLIENTS</h2>
  <div class="trust-item" style="left:121px">
    <div class="trust-icon"><svg width="70" height="70" viewBox="0 0 70 70" fill="none" stroke="#fff" stroke-width="4"><path d="M22 36c-6-7-10-12-10-18a10 10 0 0 1 20 0c0 6-4 11-10 18z"/><circle cx="22" cy="18" r="3.5"/><path d="M22 40c0 10 24 2 24 14"/><path d="M52 62c-4-5-7-8-7-12a7 7 0 0 1 14 0c0 4-3 7-7 12z" fill="#fff"/></svg></div>
    <h3>24/7 ELD TRACKING</h3>
    <p>Lorem ipsum dolor sit amet, consectetur adipiscing elit, sed &nbsp;incididunt &nbsp;magna aliqua.</p>
  </div>
  <div class="trust-item" style="left:464px">
    <div class="trust-icon"><svg width="76" height="70" viewBox="0 0 76 70" fill="#fff"><path d="M4 22a50 50 0 0 1 68 0L38 52z"/><circle cx="38" cy="60" r="5"/></svg></div>
    <h3>QUICK COVERAGE</h3>
    <p>Lorem ipsum dolor sit amet, consectetur adipiscing elit, sed &nbsp;incididunt &nbsp;magna aliqua.</p>
  </div>
  <div class="trust-item" style="left:807px">
    <div class="trust-icon"><svg width="70" height="70" viewBox="0 0 70 70" fill="#fff"><path d="M35 8 60 20 35 32 10 20z"/><path d="M8 24l25 12v26L8 50z"/><path d="M62 24 37 36v26l25-12z"/><path d="M20 14l25 12v8l-6-3v-6L14 17z" fill="#b43a5a"/></svg></div>
    <h3>ON-TIME DELIVERIES</h3>
    <p>Lorem ipsum dolor sit amet, consectetur adipiscing elit, sed &nbsp;incididunt &nbsp;magna aliqua.</p>
  </div>
</section>

<section class="survey">
  <div class="survey-photo"><div role="img" aria-label="Photo of a driver holding papers beside a white semi truck"></div></div>
  <h2 class="display">START OUR SEURVEY</h2>
  <p class="survey-copy">Lorem ipsum dolor sit amet, consectetur adipiscing elit, sed do eiusmod tempor incididunt ut labore et dolore magna aliqua. Ut enim ad minim veniam, quis nostrud exercitation ullamco laboris nisi ut aliquip ex ea commodo consequat. Duis aute irure dolor in reprehenderit in voluptate velit esse cillum dolore eu fugiat nulla pariatur. Excepteur sint occaecat cupidatat non proident, sunt in culpa qui officia deserunt mollit anim id est laborum.</p>
  <div class="btn-red">READ MORE</div>
</section>

<section class="contact" role="img" aria-label="Red tinted background photo of parked trucks">
  <h2 class="display">CONTACT US</h2>
  <div class="field" style="left:103px;top:161px">Name*</div>
  <div class="field" style="left:440px;top:161px">Email*</div>
  <div class="field" style="left:778px;top:161px">Phone*</div>
  <div class="field" style="left:103px;top:224px">Departure Location*</div>
  <div class="field" style="left:440px;top:224px">Delivery Location*</div>
  <div class="field" style="left:778px;top:224px">Commodity*</div>
  <div class="field message" style="left:103px;top:288px">Messge</div>
  <div class="btn-submit">SUBMIT</div>
</section>

<footer class="site-footer">
  <div class="foot-brand">
    <div class="foot-mark"></div>
    <div class="foot-name">BRAVO FREIGHTWAY</div>
    <div class="foot-tag">Freight Brokerage Business</div>
    <p class="foot-about">Lorem ipsum dolor sit amet, &nbsp;elit sed do eiusmod tempor incididunt ut labore et dolore magna aliqua.</p>
  </div>
  <div class="foot-col" style="left:414px">
    <h4>QUICK LINK</h4>
    <ul><li>Home</li><li>Shippers</li><li>Carriers</li><li>About</li><li>Contact Us</li></ul>
  </div>
  <div class="foot-col" style="left:590px">
    <h4>HELP LINK</h4>
    <ul><li>Privacy Policy</li><li>Terms &amp; Conditions</li></ul>
  </div>
  <div class="foot-col" style="left:795px">
    <h4>CONTACT INFO</h4>
    <div class="contact-info">
      <div class="row"><svg width="11" height="14" viewBox="0 0 11 14"><path d="M5.5 14C2 9.5 0 7.5 0 5.5a5.5 5.5 0 0 1 11 0c0 2-2 4-5.5 8.5z" fill="#1442a8"/><circle cx="5.5" cy="5.3" r="2" fill="#fff"/></svg><div><b>Main Office :</b><br>Bravo Freightway, LLC 418 Harbor Ave Suite 210, Tacoma, WA 98402</div></div>
      <div class="ind"><b>Satellite Office :</b><br>2740 Lindell Rd Suite 88, Olympia, WA 98501</div>
      <div class="row"><svg width="12" height="12" viewBox="0 0 12 12"><path d="M2.5 0 4.5 3 3.2 4.5a8 8 0 0 0 4.3 4.3L9 7.5l3 2-1 2.2C5 12 0 7 .3 1z" fill="#1442a8"/></svg><div><b>Toll Free :</b> 1-800-555-0147</div></div>
      <div class="ind"><b>Local:</b> 509-555-0162</div>
      <div class="row" style="margin-top:6px"><svg width="12" height="12" viewBox="0 0 12 12" fill="#1442a8"><rect x="2" y="0" width="8" height="4"/><rect x="0" y="4" width="12" height="6" rx="1"/><rect x="3" y="8" width="6" height="4" fill="#fff" stroke="#1442a8"/></svg><div><b>Fax :</b> 509-555-0189</div></div>
      <div class="row" style="margin-top:6px"><svg width="13" height="10" viewBox="0 0 13 10"><rect width="13" height="10" rx="1" fill="#1442a8"/><path d="M1 1l5.5 4.5L12 1" fill="none" stroke="#fff"/></svg><div><b>Email:</b> support@bravofreightway.example</div></div>
    </div>
  </div>
  <div class="foot-rule"></div>
  <div class="copyright">©Copyrights 2023 Bravo Freightway | All Rights Reserved</div>
</footer>

</body>
</html>
```